40-year-old commercial construction firm :: Business Card Revamp

We are a 40 year-old, private general construction company based in Dallas, Texas, and we are considering updating our business cards, which could lead to a larger "brand refresh" campaign.

We work in a competitive environment, selling to business owners and executives making large scale purchasing decisions on behalf of their firms. A majority of our business is repeat business, with a long sales-cycle; while business can be difficult to identify and land, the effort is often rewarded with multiple projects.

We are open to a logo "refresh" as well as designs that incorporate the existing logo.

Target Market(s)

B2B selling to business owners/executives/end users who make facility decisions for their firms.

Industry/Entity Type

Construction Company

Contact Information for Business Card

Refresh from the example provided

Logo Text

Tarnell Building Company :: See card example

Font styles to use
Other font styles liked:
• See sample card :: Designers to choose

Colors

Designer to choose colors to be used in the design.

Requirements
Must have
• Design should convey:
• Confidence
• Competence
• Capability
• Stability
• Tagline: Genuine Relationships :: Superior Services :: Environmentally Aware
Nice to have
• A solid design that is transferable from print to online.
• Note that we are also considering a painted-edge printing / card design
Should not have
• Too much color or whimsy. Our clients tend to be the serious type, and we work hard to present a serious, professional presence in the marketplace.

```html
<!DOCTYPE html>
<html lang="en">
<head>
<meta charset="utf-8">
<title>Tarnell Building Company – Stationery</title>
<link href="https://fonts.googleapis.com/css2?family=Rubik:wght@500;600&family=Roboto:wght@300;400;500&display=swap" rel="stylesheet">
<style>
  :root{
    --navy:#221d5e;
    --gold:#c19a2e;
    --paper:#ffffff;
    --ink:#222228;
    --backdrop:#858585;
    --muted:#55555f;
  }
  *{margin:0;padding:0;box-sizing:border-box}
  html,body{width:1200px;height:1200px;overflow:hidden}
  body{background:var(--backdrop);font-family:"Roboto",sans-serif;color:var(--ink);position:relative}

  .brand{display:flex;align-items:center;gap:.35em;font-family:"Rubik",sans-serif;font-weight:600;white-space:nowrap;line-height:1}
  .brand-dot{width:.9em;height:.9em;border-radius:50%;background:var(--gold);flex:none}

  .hero-brand{position:absolute;left:0;right:0;top:150px;justify-content:center;font-size:44px;color:#fff}

  /* Letterhead */
  .letterhead{position:absolute;left:100px;top:418px;width:478px;height:636px;background:var(--paper);overflow:hidden}
  .letterhead .brand{position:absolute;left:22px;top:42px;font-size:14px;color:var(--navy)}
  .lh-address{position:absolute;right:22px;top:37px;display:flex;gap:6px;font-size:6.4px;line-height:1.35}
  .lh-address .label{color:var(--gold);font-weight:500;text-align:right;text-transform:uppercase}
  .lh-address .lines p{margin-bottom:3px}
  .lh-body{position:absolute;left:55px;top:138px;width:344px;font-size:8.2px;line-height:15.3px;text-align:justify}
  .lh-body p{margin-bottom:9px}
  .lh-body .salute{margin-bottom:18px}
  .lh-sign{position:absolute;left:55px;top:424px;font-size:8.2px;line-height:15.3px}
  .signature{display:block;width:110px;height:36px;margin:2px 0 18px -14px;background:#f1f1f4}
  .lh-foot{position:absolute;left:0;bottom:0;width:478px;height:68px}
  .lh-url{position:absolute;right:22px;bottom:34px;font-size:11px;font-weight:500;color:var(--gold)}

  /* Business cards */
  .card{position:absolute;width:360px;height:210px;overflow:hidden}
  .card-front{left:784px;top:364px;background:var(--paper)}
  .card-front .curve{position:absolute;inset:0}
  .card-front .brand{position:absolute;left:22px;top:24px;width:180px;font-size:17px;line-height:1.1;color:var(--navy);white-space:normal;align-items:flex-start}
  .card-front .brand-dot{margin-top:.12em}
  .cf-office{position:absolute;left:70px;top:90px;font-size:8.6px;line-height:13.5px;font-weight:300;color:var(--muted)}
  .cf-office .label{font-weight:500;color:var(--gold);font-size:7.2px;text-transform:uppercase;margin-bottom:1px}
  .cf-office .gap{margin-top:3px}
  .cf-person{position:absolute;right:24px;top:90px;text-align:right;color:#fff;font-size:8.6px;line-height:13.5px;font-weight:300}
  .cf-person .name{font-weight:500}
  .cf-person .gap{margin-top:3px}
  .cf-url{position:absolute;right:24px;bottom:22px;font-size:8.6px;font-weight:500;color:var(--gold)}

  .card-back{left:786px;top:618px;height:212px;background:var(--navy);display:flex;align-items:center;justify-content:center}
  .card-back .brand{font-size:16px;color:#fff}
</style>
</head>
<body>

<div class="brand hero-brand"><span class="brand-dot"></span>Tarnell Building Company</div>

<article class="letterhead">
  <div class="brand"><span class="brand-dot"></span>Tarnell Building Company</div>
  <div class="lh-address">
    <div class="label">U.S. Corporate<br>Office</div>
    <div class="lines">
      <p>1187 Corvell Lane<br>Dallas, Texas 75230</p>
      <p>Main 972.555.0148</p>
      <p>Fax 972.555.0162</p>
    </div>
  </div>
  <div class="lh-body">
    <p class="salute">Dear Customers,</p>
    <p>Tur minus excerferciis ut experatusam est, officiis aut fugiatibus am necerit ipisqua ectatem perate omnihil intissuntia volupta tiuscil lamusam num vide corero cus aut et, temporro experum ipisciis atet quamus eatios et quas re voluptatem consequ assendae. Bus, sam quat aribea nes as min ped eaquat odignis tiberes ullibus et pe doles volor mo di nobis ent autaspe rumentis es min por aut et eseculp arionse ditatus digendi gniatur?</p>
    <p>Qui cus corioremped eossendam exceatibus, nulluptas num inum abor repudae vello explibus elicab idigendissin ne voluptam sincips anditasitio di temped et velicitas quamus accab ilique doluptatem landae quias ate pa voluptaquis eaquam qui commolum idendit ipsusci psamusani conet latur, net volo denit re dendand elibusam ipsusa is.</p>
    <p>Laturiorem vidiae nulpa sin eum quas et fugiatur? Temporios ellanis totatem eiciis sit rera autas accupta ad maior as peliqui quate rera eiurior aditate la sam que sin nus et optatiatia ipsunt endessus parcia core pari ut mod que num facea quibus cum et estinimilles alitatur a doluptur a aut facia core cullaut atatiorum, consequi ulluptas isquo mo voluptatesti ut.</p>
  </div>
  <div class="lh-sign">
    Best regards,
    <span class="signature" role="img" aria-label="Handwritten signature"></span>
    Dana Whitfield<br>Business Development
  </div>
  <svg class="lh-foot" viewBox="0 0 478 68" preserveAspectRatio="none" aria-hidden="true">
    <path d="M175 68 Q330 12 478 0 L478 68 Z" fill="var(--navy)"/>
  </svg>
  <div class="lh-url">tarnell.com</div>
</article>

<section class="card card-front">
  <svg class="curve" viewBox="0 0 360 210" aria-hidden="true">
    <path d="M232 0 Q212 130 256 210 L360 210 L360 0 Z" fill="var(--navy)"/>
  </svg>
  <div class="brand"><span class="brand-dot"></span><span>Tarnell Building<br>Company</span></div>
  <div class="cf-office">
    <div class="label">U.S. Corporate Office</div>
    1187 Corvell Lane<br>Dallas, Texas 75230
    <div class="gap">Main 972.555.0148</div>
    <div class="gap">Fax 972.555.0162</div>
  </div>
  <div class="cf-person">
    <div class="name">Dana Whitfield</div>
    Business Development
    <div class="gap">Cell 214.555.0193</div>
    <div class="gap">dwhitfield@tarnell.com</div>
  </div>
  <div class="cf-url">tarnell.com</div>
</section>

<section class="card card-back">
  <div class="brand"><span class="brand-dot"></span>Tarnell Building Company</div>
</section>

</body>
</html>
```